Flyer-Design für Business Center
Zielgruppe
Wir sind Co-Working /Business Center Anbieter auf Basis eines Mitgliedschaft Konzeptes. Bei uns kann man Arbeitsplätze und Büroräume mit Kaffee und Wasser in einer Lounge anmieten. Dazu bieten wir Bedarfsgerechte Mitgliedschaften an. Unsere Kunden sind Kreative, Programmierer, Freiberufler aber auch größere Unternehmen.
Aufgabenstellung
DIN LANG A 4, der Flyer wird gedruckt und kommt in Aussteller. Er soll als Eye Catcher den Preis ab 69,90 für 4 Wochen beinhalten. In diesem Preis ist alles inclusive. Also Wasser, Kaffee, Cappuccino, Drucker, Kopierer, Möbel, Putzfrau, Schreibtisch. Bürostuhl. Gleichzeitig soll der Flyer auch als PDF versendet werden können.
Weitere Information findet man auf unserer Webseite www.kranichfeldwerk.com

```html
<!DOCTYPE html>
<html lang="de">
<head>
<meta charset="utf-8">
<title>Flyer Co-Working Space – Vorder- und Rückseite</title>
<link rel="stylesheet" href="https://fonts.googleapis.com/css2?family=Barlow+Semi+Condensed:wght@400;500;600&display=swap">
<style>
  :root {
    --sky: #0fa0d9;
    --sky-soft: #5cc2ec;
    --sky-faint: #3db3e5;
    --paper: #ffffff;
    --sun: #fde400;
    --stage: #e4e4e4;
    --ink-grey: #7a7a7a;
    --bee-tone: #2a2a2a;
  }
  * { box-sizing: border-box; margin: 0; padding: 0; }
  html, body { width: 1200px; height: 3601px; overflow: hidden; }
  body {
    background: var(--stage);
    font-family: "Barlow Semi Condensed", "Arial Narrow", sans-serif;
    position: relative;
  }
  .flyer {
    position: absolute;
    left: 190px;
    width: 820px;
    height: 1720px;
    background: var(--sky);
    overflow: hidden;
    box-shadow: 0 6px 24px rgba(0,0,0,.18);
  }
  .flyer--front { top: 55px; }
  .flyer--back { top: 1826px; }
  .flyer svg.shapes { position: absolute; inset: 0; width: 820px; height: 1720px; }

  .bee-art {
    position: absolute;
    background: linear-gradient(135deg, var(--sun) 0%, var(--bee-tone) 55%, #c9cbe6 100%);
    border-radius: 40px;
    opacity: .95;
  }
  .flyer--front .bee-art { left: 0; top: 0; width: 250px; height: 230px; }
  .flyer--back .bee-art { left: 430px; top: 25px; width: 370px; height: 230px; }

  .headline {
    position: absolute;
    left: 18px; top: 640px;
    color: var(--paper);
    font-weight: 500;
    font-size: 112px;
    line-height: 0.95;
    text-transform: uppercase;
    letter-spacing: -1px;
  }
  .price-badge {
    position: absolute;
    left: 478px; top: 870px;
    width: 330px; height: 330px;
    border-radius: 50%;
    background: var(--sun);
    box-shadow: 0 0 0 6px var(--sun), 0 0 0 9px #f6cf00;
    color: var(--sky);
    transform: rotate(-8deg);
    text-align: center;
  }
  .price-badge .lead { position: absolute; left: 0; right: 0; top: 34px; font-size: 42px; line-height: 0.9; }
  .price-badge .amount { position: absolute; left: 0; right: 0; top: 86px; font-size: 136px; font-weight: 500; line-height: 1; letter-spacing: -3px; }
  .price-badge .term { position: absolute; left: 30px; right: 0; top: 200px; font-size: 42px; }
  .price-badge .term b { font-size: 110px; font-weight: 500; vertical-align: -30px; margin: 0 6px; }

  .space-title {
    position: absolute;
    left: 14px; top: 1060px;
    color: var(--sky-soft);
    font-size: 178px;
    font-weight: 500;
    line-height: 0.87;
    text-transform: uppercase;
    letter-spacing: -2px;
  }
  .included {
    position: absolute;
    left: 18px; top: 1548px;
    width: 500px;
    color: var(--paper);
    font-size: 26px;
    line-height: 1.28;
    text-transform: uppercase;
    font-weight: 500;
  }
  .included .label { color: var(--sun); }
  .brand {
    position: absolute;
    right: 26px; bottom: 30px;
    display: flex; align-items: center; gap: 12px;
    color: var(--sky);
    font-size: 54px;
    font-weight: 500;
  }
  .brand .mark { width: 26px; height: 26px; background: var(--sky); }

  .intro {
    position: absolute;
    left: 30px; top: 55px;
    width: 760px;
    color: var(--sky-soft);
    font-size: 29px;
    line-height: 1.18;
    text-transform: uppercase;
    font-weight: 500;
  }
  .intro .spacer { float: right; width: 390px; height: 190px; }
  .intro strong { color: var(--paper); font-weight: 600; }

  .service-label {
    position: absolute;
    color: var(--paper);
    font-size: 27px;
    font-weight: 600;
    text-transform: uppercase;
  }
  .ready {
    position: absolute;
    left: 30px; top: 1370px;
    color: var(--sky);
    font-size: 29px;
    line-height: 1.15;
    font-weight: 600;
    text-transform: uppercase;
  }
  .contact {
    position: absolute;
    left: 30px; top: 1535px;
    color: var(--sky);
    font-size: 27px;
    line-height: 1.28;
    font-weight: 500;
    text-transform: uppercase;
  }
  .contact .heading { color: var(--ink-grey); }
  .contact dl { display: grid; grid-template-columns: 110px auto; }
</style>
</head>
<body>

<section class="flyer flyer--front" aria-label="Flyer Vorderseite">
  <svg class="shapes" viewBox="0 0 820 1720" aria-hidden="true">
    <g fill="none" stroke="#ffffff" stroke-width="32" stroke-linejoin="miter">
      <polygon points="605,125 537.5,8 402.5,8 335,125 402.5,242 537.5,242"/>
      <polygon points="415,315 320,150 130,150 35,315 130,480 320,480"/>
      <polygon points="805,440 710,275 520,275 425,440 520,605 710,605"/>
    </g>
    <polygon points="820,1390 820,1720 420,1720" fill="#ffffff"/>
  </svg>
  <div class="bee-art" role="img" aria-label="Illustration einer Biene"></div>

  <h1 class="headline">Nur arbeiten<br>müssen Sie<br>selber!</h1>

  <div class="price-badge">
    <div class="lead">schon<br>ab</div>
    <div class="amount">69,90</div>
    <div class="term">für<b>4</b>Wochen</div>
  </div>

  <div class="space-title">Co<br>Working<br>Space</div>

  <p class="included"><span class="label">Im Preis enthalten:</span> Wasser, Kaffee, Cappuccino, Drucker, Kopierer, Möbel, Putzfrau, Schreibtisch, Bürostuhl</p>

  <div class="brand"><span class="mark"></span><span>kranichfeld</span></div>
</section>

<section class="flyer flyer--back" aria-label="Flyer Rückseite">
  <svg class="shapes" viewBox="0 0 820 1720" aria-hidden="true">
    <g fill="none" stroke="#3db3e5" stroke-width="20">
      <polygon points="720,620 620,450 420,450 320,620 420,790 620,790"/>
      <polygon points="330,1180 255,1050 105,1050 30,1180 105,1310 255,1310"/>
    </g>
    <g fill="#ffffff">
      <polygon points="298,760 248,673 148,673 98,760 148,847 248,847" role="img" aria-label="Kaffee"/>
      <polygon points="478,862 428,775 328,775 278,862 328,949 428,949" role="img" aria-label="Bürostuhl"/>
      <polygon points="674,979 624,892 524,892 474,979 524,1066 624,1066" role="img" aria-label="Kopierer"/>
      <polygon points="298,968 248,881 148,881 98,968 148,1055 248,1055" role="img" aria-label="Reinigung"/>
      <polygon points="478,1069 428,982 328,982 278,1069 328,1156 428,1156" role="img" aria-label="Wasser"/>
      <polygon points="674,1193 624,1106 524,1106 474,1193 524,1280 624,1280" role="img" aria-label="Möbel"/>
    </g>
    <g fill="none" stroke="#0fa0d9" stroke-width="7" stroke-linecap="round" stroke-linejoin="round">
      <!-- cup -->
      <path d="M160 740 h60 v28 a30 30 0 0 1 -60 0 z"/>
      <path d="M220 748 h10 a12 12 0 0 1 0 24 h-12"/>
      <path d="M150 805 h90"/>
      <path d="M178 720 v-12 M192 720 v-12 M206 720 v-12"/>
      <!-- chair -->
      <rect x="350" y="815" width="56" height="50" rx="10"/>
      <path d="M340 875 h76 M378 875 v30 M352 915 l26 -10 l26 10 M330 848 v24 M426 848 v24"/>
      <!-- copier -->
      <rect x="540" y="940" width="70" height="80" rx="4"/>
      <path d="M540 965 h70 M555 925 l50 -10 M548 1030 v12 M602 1030 v12"/>
      <!-- broom -->
      <path d="M230 910 l-60 60"/>
      <path d="M170 970 l-25 10 l10 25 l25 -10 z"/>
      <circle cx="232" cy="1000" r="4"/>
      <!-- bottle -->
      <path d="M370 1015 h16 v12 l10 14 v70 h-36 v-70 l10 -14 z"/>
      <path d="M360 1060 h36 M360 1080 h36"/>
      <!-- desk -->
      <path d="M520 1160 h110 M530 1160 v70 M620 1160 v70 M590 1160 v50 h30 M598 1185 h12"/>
    </g>
    <polygon points="0,1270 0,1720 820,1720" fill="#ffffff"/>
  </svg>
  <div class="bee-art" role="img" aria-label="Illustration eines Bienenschwarms"></div>

  <p class="intro">
    <span class="spacer"></span>
    <strong>Machen Sie es wie die Bienen: sein Sie fleissig und das zusammen!</strong>
    Als neues Unternehmen im Bereich Co-Working und Business Center verfügt unser Team dennoch über lange Erfahrung und zahlreiche Erfolgsgeschichten zurück. Unsere Mission besteht darin, Büroraum effizient und günstig nutzbar sowie zugänglich zu machen. Mit unseren Membership Konzept können user direkt durchstarten. Dabei behalten Sie die notwendige Flexibilität. <strong>Folgende Leistungen sind im Preis inklusive:</strong>
  </p>

  <span class="service-label" style="left:150px; top:620px;">Kaffee</span>
  <span class="service-label" style="left:388px; top:733px;">Bürostuhl</span>
  <span class="service-label" style="left:580px; top:848px;">Kopierer</span>
  <span class="service-label" style="left:135px; top:1060px;">Reinigung</span>
  <span class="service-label" style="left:340px; top:1162px;">Wasser</span>
  <span class="service-label" style="left:540px; top:1283px;">Möbel</span>

  <p class="ready">Ihr<br>Büroplatz<br>steht schon<br>bereit!</p>

  <div class="contact">
    <p class="heading">Kontakt:</p>
    <dl>
      <dt>Tel.:</dt><dd>+49-211-555018-00</dd>
      <dt>Email:</dt><dd>info(at)kranichfeldwerk.com</dd>
      <dt>Web:</dt><dd>https://www.kranichfeldwerk.com</dd>
    </dl>
  </div>
</section>

</body>
</html>
```